Cole Varga Photography

Would like the Business card to have a cool logo. I’m targeting wedding/ engagement: portrait photography. My phone number on it. And my business email address.

Wedding/portrait/engagement photography.

```html
<!DOCTYPE html>
<html lang="en">
<head>
<meta charset="UTF-8">
<title>Cole Varga Photography – Business Card</title>
<link rel="stylesheet" href="https://fonts.googleapis.com/css2?family=Montserrat:wght@700&family=Alegreya+Sans:wght@400&family=Varela+Round&display=swap">
<style>
  :root {
    --backdrop: #2c3038;
    --card: #f3f3f1;
    --ink: #1c1c1c;
    --accent: #3e6389;
    --rule: #222222;
  }
  html, body {
    margin: 0;
    padding: 0;
    width: 1200px;
    height: 936px;
    overflow: hidden;
    background: var(--backdrop);
  }
  .business-card {
    position: absolute;
    left: 100px;
    top: 163px;
    width: 1000px;
    height: 610px;
    background: var(--card);
    box-shadow: 0 10px 30px rgba(0,0,0,0.35);
  }
  .brand {
    position: absolute;
    left: 0;
    right: 0;
    top: 80px;
    display: flex;
    justify-content: center;
    align-items: center;
    gap: 30px;
  }
  .brand-square {
    width: 108px;
    height: 108px;
    background: var(--ink);
  }
  .brand-name {
    font-family: "Montserrat", sans-serif;
    font-weight: 700;
    color: var(--ink);
    font-size: 40px;
    line-height: 1.05;
    letter-spacing: 1px;
    margin: 0;
  }
  .brand-name span {
    display: block;
  }
  .divider {
    position: absolute;
    left: 27px;
    right: 28px;
    top: 275px;
    height: 2px;
    background: var(--rule);
  }
  .person {
    position: absolute;
    left: 0;
    right: 0;
    top: 352px;
    text-align: center;
  }
  .person-name {
    font-family: "Alegreya Sans", sans-serif;
    font-weight: 400;
    font-size: 44px;
    color: var(--accent);
    margin: 0;
    line-height: 1;
    letter-spacing: 0.5px;
  }
  .person-role {
    font-family: "Varela Round", sans-serif;
    font-size: 24px;
    color: var(--ink);
    margin: 8px 0 0;
  }
  .contact {
    position: absolute;
    left: 0;
    right: 0;
    top: 480px;
    text-align: center;
    font-family: "Varela Round", sans-serif;
    font-size: 25px;
    color: var(--ink);
    line-height: 36px;
  }
  .contact p {
    margin: 0;
  }
  .contact .label {
    color: var(--accent);
    margin-right: 10px;
  }
</style>
</head>
<body>
  <main class="business-card">
    <header class="brand">
      <div class="brand-square"></div>
      <h1 class="brand-name"><span>COLE VARGA</span><span>PHOTOGRAPHY</span></h1>
    </header>
    <div class="divider"></div>
    <section class="person">
      <h2 class="person-name">MARA LINDQVIST</h2>
      <p class="person-role">Photographer</p>
    </section>
    <section class="contact">
      <p><span class="label">P:</span>+8000 20 20 20</p>
      <p><span class="label">E:</span>cole@vargaphotography.com</p>
    </section>
  </main>
</body>
</html>
```